Organic rose water based skincare line in need of product label and packaging design

We are looking for a simple, clean, modern labeling and packaging design for 2 of our products. Our brand's demographic is upscale females ages 20-40. We want our packaging to be very minimalistic, and instagramable.

Product #1: Rose water facial spray "Lumi Mist"
Product #2: Rose water facial toner "Velvet Hush Hour"

Please see attached images for our current logo and label design. We have also added some images that inspire our branding.

Target Market(s)

trendy woman ages 20-40

Industry/Entity Type

Skin Care Product

Font styles to use
Serif
Sans Serif

Colors

Designer to choose only greyscale colors for use in the design.

Requirements
Must have
• Must have our logo, bottle size, product name on front and how to use and ingredient on the back. Please see project description and attached images for more information.
Should not have
• Too much going on or too many colors.

```html
<!DOCTYPE html>
<html lang="en">
<head>
<meta charset="utf-8">
<title>Lumi Mist – Label Set</title>
<link href="https://fonts.googleapis.com/css2?family=Montserrat:wght@200;300;500&family=Allura&family=Mrs+Saint+Delafield&display=swap" rel="stylesheet">
<style>
  :root {
    --paper: #ffffff;
    --label: #fbfbfb;
    --wash-light: #f1f1f1;
    --wash-deep: #dedede;
    --tone-text: #8c8c8c;
    --tone-line: #c4c4c4;
    --edge: #9e9e9e;
    --ink: #3a3a3a;
  }
  * { margin: 0; padding: 0; box-sizing: border-box; }
  html, body { width: 1200px; height: 1200px; overflow: hidden; background: var(--paper); }
  .canvas { position: relative; width: 1200px; height: 1200px; }

  .label {
    position: absolute; top: 275px; width: 440px; height: 650px;
    background: var(--label); overflow: hidden;
    box-shadow: 0 2px 10px rgba(0,0,0,0.06);
  }
  .label--front { left: 140px; }
  .label--back { left: 620px; }

  .label__wash { position: absolute; inset: 0; width: 440px; height: 650px; }
  .floral { position: absolute; border-radius: 40% 50% 45% 55%;
    background: radial-gradient(circle, rgba(180,180,180,0.28), rgba(180,180,180,0) 70%); }

  .brand-mark {
    position: absolute; left: 26px; top: 26px; display: flex; align-items: center; gap: 8px;
    font-family: "Montserrat", sans-serif; font-weight: 500; font-size: 12px;
    letter-spacing: 3px; text-transform: uppercase; color: var(--ink);
  }
  .brand-mark__dot { width: 8px; height: 8px; border-radius: 50%; background: var(--ink); }

  .front__name {
    position: absolute; left: 62px; top: 300px;
    font-family: "Montserrat", sans-serif; font-weight: 200;
    color: var(--tone-text); font-size: 76px; line-height: 68px;
  }
  .front__tagline {
    position: absolute; left: 59px; top: 468px;
    font-family: "Mrs Saint Delafield", cursive; font-size: 22px; color: var(--ink);
  }
  .front__size {
    position: absolute; left: 59px; top: 578px;
    font-family: "Montserrat", sans-serif; font-weight: 500; font-size: 20px; color: var(--tone-text);
  }

  .back__line-note {
    position: absolute; left: 26px; top: 26px;
    font-family: "Montserrat", sans-serif; font-weight: 300; font-size: 12px;
    letter-spacing: 2px; text-transform: uppercase; color: var(--ink);
  }
  .back__title {
    position: absolute; left: 60px; top: 266px;
    font-family: "Allura", cursive; font-size: 44px; line-height: 50px; color: var(--tone-text);
  }
  .back__usage {
    position: absolute; left: 60px; top: 346px;
    font-family: "Montserrat", sans-serif; font-weight: 300; font-size: 23px; line-height: 26px;
    color: var(--tone-text);
  }
  .back__ingredient {
    position: absolute; left: 60px; top: 446px;
    font-family: "Mrs Saint Delafield", cursive; font-size: 32px; line-height: 40px;
    color: var(--ink); word-spacing: 4px;
  }
  .back__benefits {
    position: absolute; left: 60px; top: 510px; list-style: none;
    font-family: "Montserrat", sans-serif; font-weight: 300; font-size: 15.5px; line-height: 19.5px;
    color: var(--tone-text);
  }
</style>
</head>
<body>
<main class="canvas">

  <section class="label label--front">
    <svg class="label__wash" viewBox="0 0 440 650" role="img" aria-label="Soft grey watercolour wash with fine torn edge">
      <defs>
        <linearGradient id="washFront" x1="0" y1="0" x2="1" y2="1">
          <stop offset="0" stop-color="#f4f4f4"/>
          <stop offset="1" stop-color="#dcdcdc"/>
        </linearGradient>
      </defs>
      <path d="M0 0 H440 V292 C415 300 395 296 375 288 C340 262 300 236 265 190 C230 150 195 135 160 112 C120 98 70 96 0 85 Z" fill="url(#washFront)"/>
      <path d="M0 85 C70 96 120 98 160 112 C195 135 230 150 265 190 C300 236 340 262 375 288 C395 296 415 300 440 292" fill="none" stroke="var(--edge)" stroke-width="2"/>
    </svg>
    <div class="floral" role="img" aria-label="Line drawing of rose blossoms" style="left:215px;top:0;width:225px;height:195px;"></div>
    <div class="floral" role="img" aria-label="Line drawing of rose blossoms" style="left:235px;top:510px;width:205px;height:140px;"></div>

    <div class="brand-mark"><span class="brand-mark__dot"></span>Lumi Mist</div>
    <h1 class="front__name">lumi<br>Mist</h1>
    <p class="front__tagline">Organic Rosewater Hydrating Mist</p>
    <p class="front__size">2 oz / 60 ml</p>
  </section>

  <section class="label label--back">
    <svg class="label__wash" viewBox="0 0 440 650" role="img" aria-label="Soft grey watercolour wash with fine torn edge">
      <defs>
        <linearGradient id="washBack" x1="0" y1="0" x2="1" y2="1">
          <stop offset="0" stop-color="#f4f4f4"/>
          <stop offset="1" stop-color="#dcdcdc"/>
        </linearGradient>
      </defs>
      <path d="M0 0 H440 V285 C420 290 405 305 385 300 C350 282 320 250 290 200 C255 160 215 140 175 120 C130 105 70 98 0 82 Z" fill="url(#washBack)"/>
      <path d="M0 82 C70 98 130 105 175 120 C215 140 255 160 290 200 C320 250 350 282 385 300 C405 305 420 290 440 285" fill="none" stroke="var(--edge)" stroke-width="2"/>
    </svg>
    <div class="floral" role="img" aria-label="Line drawing of rose blossoms" style="left:320px;top:380px;width:120px;height:270px;"></div>
    <div class="floral" role="img" aria-label="Line drawing of rose blossom" style="left:-10px;top:590px;width:40px;height:60px;"></div>

    <p class="back__line-note">Also in the line · Velvet Hush Hour</p>
    <h2 class="back__title">Mist Over</h2>
    <p class="back__usage">face + body + hair<br>as desired for hydration</p>
    <p class="back__ingredient">Organic . Rose . Water</p>
    <ul class="back__benefits">
      <li>+ hydrates</li>
      <li>+ fights acne</li>
      <li>+ maintains skin's pH</li>
      <li>+ strengthens skin cells</li>
      <li>+ prevents fine lines &amp; wrinkles</li>
    </ul>
  </section>

</main>
</body>
</html>
```